New design for a company based in SF called Lumo Ride. People rent out our cars and we would like to create a subscription based platform to rent out our cars.
We rent out cars through ride share hub and vexa and would like people to be able to book or be redirected from our site.
Platform
I would like to have three interface.
Here are the things we need;
First interface
Company side where we can custom pricing of level subscription
level one classic; level two premiere; level 3 premium,
Second Interface-
User subscribing to the car
A subscription of low, medium, and premium
-each level needs to be based on how much miles they use per year.
-Insurance selected
This will be a custom delivery service on car
-Provide a drop off time
-minimum 1 hour notice
Third Interface
Peer to Peer Drop off-
Have people who want to get paid and select what car they would like to pick up and drop off
Create algorithm for each price to drop off due to time and distance from it destination
Updates
Need extra days to review
I emailed support and it took them 5 days to respond to find out that the designer who we select for our web design is the same designer for our logo. I need the 5 extra days because I need to fix the logo now. Thank you
Target Market(s)
domestic and international tourists travelling to San Francisco bay area-
Industry/Entity Type
Travel Industry
Logo Text
Either the name Lumo Ride or LR. I would like it to have a message within the Logo. https://www.plorvex.com/learn/hidden-meanings-behind-50-worlds-recognizable-logos/ Similar to Quibly,
Coding
Coded - Design and coding required
Number of Pages Required
1 page
Requirements
Must have
- page with what level subscription they need; Classic; Premiere, Premium
Nice to have
- calendar of availability

```html
<!DOCTYPE html>
<html lang="en">
<head>
<meta charset="utf-8">
<title>Lumo Ride — Car Subscription</title>
<link href="https://fonts.googleapis.com/css2?family=Lato:wght@400;700;900&family=Open+Sans:wght@400;600;700&display=swap" rel="stylesheet">
<style>
:root{
  --blue:#1f6fe0;
  --blue-dark:#1857b8;
  --orange:#ff7a00;
  --orange-dark:#e96a00;
  --ink:#222;
  --text:#666;
  --muted:#999;
  --line:#dcdcdc;
  --light:#f1f1f1;
  --footer:#1c1c1e;
  --footer-bottom:#121213;
  --white:#fff;
}
*{box-sizing:border-box;margin:0;padding:0}
html,body{width:1200px;height:5187px;overflow:hidden}
body{font-family:"Open Sans",Arial,sans-serif;color:var(--text);background:var(--white);position:relative}
section,header,footer{position:relative;width:1200px;overflow:hidden}
h2{font-family:"Lato",Arial,sans-serif;font-weight:900;text-transform:uppercase;color:var(--ink);letter-spacing:.5px}
.abs{position:absolute}
.btn{display:inline-block;font-family:"Lato",Arial,sans-serif;font-weight:700;text-transform:uppercase;text-align:center;color:var(--white)}

/* header */
.site-header{height:97px;background:var(--white);box-shadow:0 2px 6px rgba(0,0,0,.08);z-index:2}
.brand{left:104px;top:22px;display:flex;align-items:center;gap:12px}
.brand-dot{width:52px;height:52px;border-radius:50%;background:var(--blue)}
.brand-name{font-family:"Lato",Arial,sans-serif;font-weight:900;font-size:32px;color:var(--blue)}
.main-nav{right:98px;top:40px;display:flex;gap:28px;font-size:16px;color:#444}
.main-nav .active{color:var(--orange)}

/* hero */
.hero{height:593px}
.hero-photo{left:0;top:0;width:1200px;height:560px;background:linear-gradient(180deg,#8fb6cf 0%,#6f8f8a 40%,#3b3b3e 75%,#2a2a2c 100%)}
.hero-shade{left:0;top:0;width:1200px;height:560px;background:rgba(0,0,0,.25)}
.hero-title{left:0;top:214px;width:1200px;text-align:center;font-family:"Lato",Arial,sans-serif;font-weight:900;font-size:54px;line-height:58px;color:var(--white);text-transform:uppercase}
.hero-btn{left:503px;top:332px;width:200px;height:40px;line-height:40px;background:var(--orange);border-radius:3px;font-size:18px;text-transform:none}
.hero-arrow{top:236px}
.hero-wave{left:0;bottom:0}

/* about */
.about{height:450px;text-align:center}
.about h2{padding-top:115px;font-size:31px}
.about p{width:820px;margin:22px auto 0;font-size:16px;line-height:26px;color:var(--muted)}
.about p+p{margin-top:14px}
.about .btn{margin-top:26px;width:172px;height:40px;line-height:40px;background:var(--blue);text-transform:none;font-size:16px;border-radius:2px}

/* why */
.why{height:570px}
.why-photo{left:363px;top:20px;width:837px;height:532px;background:linear-gradient(160deg,#9bb38a 0%,#6f8e58 35%,#a4a7a3 60%,#d8dad6 100%)}
.why-panel{left:0;top:88px;width:668px;height:380px;background:var(--orange);border-radius:0 190px 190px 0;padding:64px 0 0 125px;color:var(--white)}
.why-panel h2{color:var(--white);font-size:30px;font-weight:700}
.why-panel p{width:430px;font-size:15px;line-height:24px;margin-top:14px;color:#ffe6cf}
.why-panel .btn{margin-top:22px;width:170px;height:44px;line-height:40px;border:2px solid var(--white);font-size:14px}

/* plans */
.plans{height:500px;text-align:center}
.plans h2{padding-top:40px;font-size:26px;font-weight:700}
.plan{top:105px;width:311px;height:335px;border:1px solid var(--line);box-shadow:0 1px 4px rgba(0,0,0,.06);padding:30px 28px 0;text-align:center}
.plan svg{display:block;margin:0 auto}
.plan h3{font-family:"Lato",Arial,sans-serif;font-weight:900;color:var(--blue);font-size:22px;margin-top:12px;text-transform:uppercase}
.plan p{font-size:12px;line-height:17px;color:var(--muted);margin-top:8px}
.plan .btn{margin-top:26px;width:250px;height:40px;line-height:40px;background:var(--orange);font-size:14px}

/* calendar */
.schedule{height:615px;background:linear-gradient(90deg,#c9c9c9 0%,#ececec 25%,#f3f3f3 60%,#d9d9d9 100%)}
.schedule-title{left:173px;top:80px;width:415px;text-align:center;font-size:30px;font-weight:700}
.calendar{left:173px;top:135px;width:415px}
.cal-head{height:41px;background:var(--white);display:flex;justify-content:center;align-items:center;gap:60px;font-family:"Lato",Arial,sans-serif;font-weight:900;color:var(--blue);font-size:22px}
.cal-grid{display:grid;grid-template-columns:repeat(7,1fr);gap:2px;background:var(--white)}
.cal-grid span{height:50px;line-height:50px;text-align:center;color:var(--white);font-size:17px;font-weight:600;background:var(--blue)}
.cal-grid .dow{height:34px;line-height:34px;background:#333;font-size:13px}
.cal-grid .b{background:var(--orange)}
.cal-grid .e{background:transparent}
.legend{left:242px;top:545px;display:flex;gap:40px;font-family:"Lato",Arial,sans-serif;font-weight:700;font-size:15px;color:#444}
.legend i{display:inline-block;width:22px;height:22px;border-radius:50%;vertical-align:middle;margin-right:10px}
.booking{left:633px;top:65px;width:532px;height:455px;background:var(--white);border:1px solid var(--line);padding:28px 48px}
.booking h3{font-family:"Lato",Arial,sans-serif;font-weight:700;font-size:27px;color:var(--ink);text-align:center;text-transform:uppercase}
.field{height:44px;border:1px solid var(--line);margin-top:12px;padding-left:16px;line-height:42px;font-size:13px;color:#777}
.booking .first{margin-top:22px}
.field-row{display:flex;gap:14px}
.field-row .field{flex:1;display:flex;align-items:center;gap:8px}
.booking .btn{display:block;margin-top:18px;height:46px;line-height:46px;background:var(--orange);font-size:16px}

/* how it works */
.how{height:453px;background:var(--orange);text-align:center;color:var(--white)}
.how h2{color:var(--white);padding-top:58px;font-size:32px;font-weight:700}
.how .sub{font-size:17px;margin-top:4px}
.step{top:170px;width:200px;text-align:center}
.step-art{width:136px;height:136px;border-radius:50%;background:radial-gradient(circle,#f3f3f3 0%,#ffffff 70%);border:3px solid var(--white);margin:0 auto}
.step h4{margin-top:20px;font-family:"Lato",Arial,sans-serif;font-weight:900;font-size:17px;line-height:22px;text-transform:uppercase}
.how-links{left:0;top:180px}

/* subscribe */
.subscribe{height:500px}
.sub-photo{left:0;top:0;width:1200px;height:500px;background:linear-gradient(180deg,#3a7fd0 0%,#6aa9e6 35%,#1e6ab8 55%,#1a4f88 80%,#7a6350 100%)}
.subscribe h2{left:0;top:150px;width:1200px;text-align:center;color:var(--white);font-size:34px;line-height:40px;font-weight:900}
.sub-form{left:287px;top:250px;display:flex}
.sub-input{width:460px;height:52px;background:var(--white);display:flex;align-items:center;gap:12px;padding-left:20px;font-size:14px;color:#666;text-transform:uppercase}
.sub-form .btn{width:135px;height:52px;line-height:52px;background:var(--orange);font-size:18px}

/* testimonials */
.testimonials{height:462px;background:#f2f2f2;text-align:center}
.testimonials h2{padding-top:66px;color:var(--blue);font-size:32px;font-weight:700}
.quote{top:147px;height:260px;width:430px;background:var(--white);box-shadow:0 1px 5px rgba(0,0,0,.1);padding:78px 40px 0}
.avatar{left:50%;top:-40px;width:90px;height:90px;margin-left:-45px;border-radius:50%;border:4px solid var(--white);background:linear-gradient(180deg,#9aa7b3,#5e6b78)}
.q-mark{font-family:"Lato",Arial,sans-serif;font-weight:900;font-size:44px;color:#bbb;line-height:26px}
.quote p{font-size:13px;line-height:18px;color:#888;margin-top:12px}
.quote .author{font-weight:700;color:#333;margin-top:14px;font-size:13px}
.stars{color:var(--orange);font-size:20px;letter-spacing:3px;margin-top:8px}
.t-arrow{top:255px}

/* blogs */
.blogs{height:545px;text-align:center}
.blogs h2{padding-top:52px;font-size:30px;font-weight:700}
.post{top:117px;width:313px;height:353px;border:1px solid var(--line);box-shadow:0 1px 4px rgba(0,0,0,.06)}
.post-photo{height:205px;background:linear-gradient(160deg,#a7b1bc,#6f7884)}
.post-date{left:50%;top:188px;margin-left:-75px;width:150px;height:32px;line-height:32px;background:var(--orange);color:var(--white);font-size:13px}
.post h3{margin-top:30px;font-family:"Lato",Arial,sans-serif;font-weight:900;font-size:18px;color:#222}
.post p{font-size:12px;line-height:16px;color:#888;padding:6px 28px 0}
.post .more{display:block;margin-top:8px;font-size:12px;font-weight:700;color:var(--blue);text-transform:uppercase}

/* footer */
.site-footer{height:330px;background:var(--footer);color:#bbb}
.f-brand{left:125px;top:80px;font-family:"Lato",Arial,sans-serif;font-weight:900;font-size:32px;color:var(--white)}
.f-about{left:125px;top:130px;width:270px;font-size:12px;line-height:17px;color:#aaa}
.socials{left:125px;top:210px;display:flex;gap:8px}
.socials span{width:34px;height:34px;border-radius:50%;border:2px solid #ddd}
.f-col{top:80px;font-size:14px;line-height:28px;color:#ccc}
.f-col h4{font-family:"Lato",Arial,sans-serif;font-weight:900;color:var(--white);font-size:17px;margin-bottom:10px;text-transform:uppercase}
.f-contact li{display:flex;gap:10px;align-items:flex-start;line-height:22px;margin-bottom:8px}
.f-col ul{list-style:none}
.f-bottom{height:72px;background:var(--footer-bottom);text-align:center;line-height:72px;font-size:12px;color:#888;border-top:1px solid #333}
</style>
</head>
<body>

<header class="site-header">
  <div class="brand abs"><span class="brand-dot"></span><span class="brand-name">Lumo Ride</span></div>
  <nav class="main-nav abs">
    <span class="active">Home</span><span>About Us</span><span>Rent Car</span><span>Calendar</span><span>Testimonial</span><span>Contact</span>
  </nav>
</header>

<section class="hero">
  <div class="hero-photo abs" role="img" aria-label="Friends with raised arms riding in an open convertible on a sunny road"></div>
  <div class="hero-shade abs"></div>
  <svg class="hero-arrow abs" style="left:52px" width="30" height="50" viewBox="0 0 30 50"><path d="M26 3 L4 25 L26 47" fill="none" stroke="#fff" stroke-width="4"/></svg>
  <svg class="hero-arrow abs" style="right:52px" width="30" height="50" viewBox="0 0 30 50"><path d="M4 3 L26 25 L4 47" fill="none" stroke="#fff" stroke-width="4"/></svg>
  <h1 class="hero-title abs">Rent out a car in a<br>few seconds</h1>
  <span class="btn hero-btn abs">Subscription</span>
  <svg class="abs" style="left:586px;top:432px" width="28" height="44" viewBox="0 0 28 44"><path d="M14 2 V40 M3 29 L14 41 L25 29" fill="none" stroke="#fff" stroke-width="3"/></svg>
  <svg class="hero-wave abs" width="1200" height="120" viewBox="0 0 1200 120">
    <path d="M0 40 C300 130 900 130 1200 40 L1200 120 L0 120 Z" fill="#fff"/>
    <path d="M0 28 C300 118 900 118 1200 28" fill="none" stroke="var(--blue)" stroke-width="16"/>
  </svg>
</section>

<section class="about">
  <h2>About Lumo Ride</h2>
  <p>Vivamus porttitor purus nisi eleifend libero a tempus libero lectus feugiat felis Morbi diam mauris Morbi porta Aibero id ullamcorper nonummy nibh ligula</p>
  <p>pulvinar metus eget consectetuer augue nisi quis lacus Ut ac mi quis lacus mollis aliquam Curabitur iaculis tempus eros Class aptent taciti sociosqu ad litora nostra per conubia nostra per inceptos hymenaeos Proin nulla arcu nonummy</p>
  <span class="btn">Learn More</span>
</section>

<section class="why">
  <div class="why-photo abs" role="img" aria-label="Woman with outstretched arms standing up in a convertible driving along a country road"></div>
  <div class="why-panel abs">
    <h2>Why choose us</h2>
    <p>Vivamus porttitor purus nisi eleifend libero a tempus libero lectus feugiat felis Morbi diam mauris Morbi</p>
    <p>pulvinar metus eget consectetuer augue nisi quis lacus Ut ac mi quis lacus mollis aliquam Curabitur iaculis tempus eros Class aptent taciti</p>
    <span class="btn">Learn More</span>
  </div>
</section>

<section class="plans">
  <h2>Select Plan</h2>
  <div class="plan abs" style="left:114px">
    <svg width="56" height="64" viewBox="0 0 56 64"><circle cx="28" cy="24" r="19" fill="none" stroke="var(--blue)" stroke-width="3"/><circle cx="28" cy="24" r="11" fill="none" stroke="var(--blue)" stroke-width="3"/><path d="M17 40 L12 60 L22 55 L26 62 L28 44 M39 40 L44 60 L34 55 L30 62 L28 44" fill="none" stroke="var(--blue)" stroke-width="3" stroke-linejoin="round"/></svg>
    <h3>Classic</h3>
    <p>Lorem ipsum dolor sit amet consectetuer adipiscing elit Nam cursus Morbi ut mi Nullam enim leo egestas id condimentum at laoreet</p>
    <span class="btn">Choose From</span>
  </div>
  <div class="plan abs" style="left:443px">
    <svg width="64" height="64" viewBox="0 0 64 64"><circle cx="32" cy="32" r="28" fill="none" stroke="var(--blue)" stroke-width="3"/><path d="M32 14 L37 26 L50 27 L40 35 L43 48 L32 41 L21 48 L24 35 L14 27 L27 26 Z" fill="none" stroke="var(--blue)" stroke-width="3" stroke-linejoin="round"/></svg>
    <h3>Premiere</h3>
    <p>Lorem ipsum dolor sit amet consectetuer adipiscing elit Nam cursus Morbi ut mi Nullam enim leo egestas id condimentum at laoreet</p>
    <span class="btn">Choose From</span>
  </div>
  <div class="plan abs" style="left:771px">
    <svg width="64" height="64" viewBox="0 0 64 64"><path d="M14 6 L32 16 L50 6 L46 22" fill="none" stroke="var(--blue)" stroke-width="3"/><circle cx="32" cy="36" r="17" fill="none" stroke="var(--blue)" stroke-width="3"/><path d="M32 27 L35 33 L41 34 L36.5 38 L38 44 L32 41 L26 44 L27.5 38 L23 34 L29 33 Z" fill="var(--blue)"/><path d="M18 50 L12 62 L22 58 M46 50 L52 62 L42 58" fill="none" stroke="var(--blue)" stroke-width="3"/></svg>
    <h3>Premium</h3>
    <p>Lorem ipsum dolor sit amet consectetuer adipiscing elit Nam cursus Morbi ut mi Nullam enim leo egestas id condimentum at laoreet</p>
    <span class="btn">Choose From</span>
  </div>
</section>

<section class="schedule" role="img" aria-label="Soft grey backdrop with faint parked cars on either side">
  <h2 class="schedule-title abs">Calendar</h2>
  <div class="calendar abs">
    <div class="cal-head"><span>&lsaquo;</span><span>NOV 2018</span><span>&rsaquo;</span></div>
    <div class="cal-grid">
      <span class="dow">MO</span><span class="dow">TU</span><span class="dow">WE</span><span class="dow">TH</span><span class="dow">FR</span><span class="dow">SA</span><span class="dow">SU</span>
      <span>1</span><span>2</span><span class="b">3</span><span class="b">4</span><span>5</span><span>6</span><span>7</span>
      <span>8</span><span class="b">9</span><span class="b">10</span><span class="b">11</span><span>12</span><span class="b">13</span><span>14</span>
      <span>15</span><span class="b">16</span><span>17</span><span class="b">18</span><span class="b">19</span><span>20</span><span>21</span>
      <span>22</span><span class="b">23</span><span class="b">24</span><span>25</span><span class="b">26</span><span>27</span><span>28</span>
      <span class="e"></span><span>30</span><span>31</span><span class="e"></span><span class="e"></span><span class="e"></span><span class="e"></span>
    </div>
  </div>
  <div class="legend abs"><span><i style="background:var(--orange)"></i>BOOKED</span><span><i style="background:var(--blue)"></i>AVAILABLE</span></div>
  <div class="booking abs">
    <h3>Booking Form</h3>
    <div class="field first">Your Name</div>
    <div class="field">Email address</div>
    <div class="field">Phone Number</div>
    <div class="field">Car</div>
    <div class="field-row">
      <div class="field"><svg width="14" height="14" viewBox="0 0 14 14"><rect x="1" y="2" width="12" height="11" fill="none" stroke="#777" stroke-width="1.5"/><path d="M1 5 H13" stroke="#777" stroke-width="1.5"/></svg>Select Date</div>
      <div class="field"><svg width="14" height="14" viewBox="0 0 14 14"><circle cx="7" cy="7" r="6" fill="none" stroke="#777" stroke-width="1.5"/><path d="M7 3 V7 L10 9" fill="none" stroke="#777" stroke-width="1.5"/></svg>Time</div>
    </div>
    <span class="btn">Book Now</span>
  </div>
</section>

<section class="how">
  <h2>How it works</h2>
  <p class="sub">Get the Perfect car in 4 easy steps and special offers</p>
  <svg class="how-links abs" width="1200" height="120" viewBox="0 0 1200 120">
    <g fill="none" stroke="#fff" stroke-width="3">
      <path d="M322 40 Q367 0 412 40"/><path d="M404 30 L412 40 L400 42"/>
      <path d="M557 40 Q602 0 647 40"/><path d="M639 30 L647 40 L635 42"/>
      <path d="M792 40 Q837 0 882 40"/><path d="M874 30 L882 40 L870 42"/>
    </g>
  </svg>
  <div class="step abs" style="left:149px"><div class="step-art" role="img" aria-label="Red car illustration"></div><h4>List your<br>car</h4></div>
  <div class="step abs" style="left:384px"><div class="step-art" role="img" aria-label="Illustration of a host answering a request"></div><h4>Respond to<br>requests</h4></div>
  <div class="step abs" style="left:619px"><div class="step-art" role="img" aria-label="Handshake illustration"></div><h4>Meet your<br>guest</h4></div>
  <div class="step abs" style="left:854px"><div class="step-art" role="img" aria-label="Red car with keys illustration"></div><h4>Pick up your<br>car</h4></div>
</section>

<section class="subscribe">
  <div class="sub-photo abs" role="img" aria-label="Traveller with open arms on a coastal road above a blue sea"></div>
  <h2 class="abs">Why subscribe to<br>Lumo Ride</h2>
  <div class="sub-form abs">
    <div class="sub-input"><svg width="18" height="14" viewBox="0 0 18 14"><rect x="1" y="1" width="16" height="12" fill="none" stroke="#888" stroke-width="1.5"/><path d="M1 1 L9 8 L17 1" fill="none" stroke="#888" stroke-width="1.5"/></svg>Email address</div>
    <span class="btn">Sign up</span>
  </div>
</section>

<section class="testimonials">
  <h2>Testimonials</h2>
  <svg class="t-arrow abs" style="left:108px" width="20" height="36" viewBox="0 0 20 36"><path d="M17 2 L3 18 L17 34" fill="none" stroke="#777" stroke-width="3"/></svg>
  <svg class="t-arrow abs" style="right:108px" width="20" height="36" viewBox="0 0 20 36"><path d="M3 2 L17 18 L3 34" fill="none" stroke="#777" stroke-width="3"/></svg>
  <div class="quote abs" style="left:156px">
    <div class="avatar abs" role="img" aria-label="Customer portrait"></div>
    <div class="q-mark">&ldquo;</div>
    <p>Nunc tempus felis vitae urna Vivamus porttitor neque at volutpat rutrum purus nisi eleifend libero a tempus libero lectu.</p>
    <p class="author">By Author Name</p>
    <div class="stars">★★★</div>
  </div>
  <div class="quote abs" style="left:608px">
    <div class="avatar abs" role="img" aria-label="Customer portrait"></div>
    <div class="q-mark">&ldquo;</div>
    <p>Nunc tempus felis vitae urna Vivamus porttitor neque at volutpat rutrum purus nisi eleifend libero a tempus libero lectu.</p>
    <p class="author">Niko Varell</p>
    <div class="stars">★★★</div>
  </div>
</section>

<section class="blogs">
  <h2>Recent Blogs</h2>
  <article class="post abs" style="left:121px">
    <div class="post-photo" role="img" aria-label="Couple smiling inside a car"></div>
    <span class="post-date abs">05 Aug 2017</span>
    <h3>Your Blog Title here</h3>
    <p>Tellus id malesuada feries ac turpis egestas cras id elit integer quis urna id elite enim dapibus malesuada fringilla.</p>
    <span class="more">Read More</span>
  </article>
  <article class="post abs" style="left:446px">
    <div class="post-photo" role="img" aria-label="Hand passing car keys"></div>
    <span class="post-date abs">05 Aug 2017</span>
    <h3>Your Blog Title here</h3>
    <p>Tellus id malesuada feries ac turpis egestas cras id elit integer quis urna id elite enim dapibus malesuada fringilla.</p>
    <span class="more">Read More</span>
  </article>
  <article class="post abs" style="left:768px">
    <div class="post-photo" role="img" aria-label="Woman at the wheel of a car"></div>
    <span class="post-date abs">05 Aug 2017</span>
    <h3>Your Blog Title here</h3>
    <p>Tellus id malesuada feries ac turpis egestas cras id elit integer quis urna id elite enim dapibus malesuada fringilla.</p>
    <span class="more">Read More</span>
  </article>
</section>

<footer class="site-footer">
  <div class="f-brand abs">Lumo Ride</div>
  <p class="f-about abs">Class aptent taciti sociosqu ad litora torquent per conubia nostra per inceptos hymenaeos Proin nibh nonummy luctus dictum eget ferme.</p>
  <div class="socials abs"><span></span><span></span><span></span><span></span></div>
  <div class="f-col abs" style="left:440px"><h4>Quick Links</h4><ul><li>Home</li><li>About Us</li><li>Rent Car</li><li>Why Us</li></ul></div>
  <div class="f-col abs" style="left:643px"><h4>Resources</h4><ul><li>Testimonials</li><li>Blogs</li><li>Calendar</li><li>Contact Us</li></ul></div>
  <div class="f-col abs" style="left:872px"><h4>Contact Us</h4>
    <ul class="f-contact">
      <li><svg width="14" height="18" viewBox="0 0 14 18"><path d="M7 17 C7 17 1 10 1 6.5 A6 6 0 0 1 13 6.5 C13 10 7 17 7 17 Z" fill="#ddd"/><circle cx="7" cy="6.5" r="2.2" fill="var(--footer)"/></svg><span>48 Harbor Lane, Suite 3<br>San Francisco CA 94107</span></li>
      <li><svg width="14" height="16" viewBox="0 0 14 16"><path d="M3 1 L6 4 L4.5 6.5 C5.5 9 7 10.5 9.5 11.5 L12 10 L13 14 C10 16 1 9 3 1 Z" fill="#ddd"/></svg><span>555.014.2098</span></li>
      <li><svg width="16" height="12" viewBox="0 0 16 12"><rect x="1" y="1" width="14" height="10" fill="none" stroke="#ddd" stroke-width="1.5"/><path d="M1 1 L8 7 L15 1" fill="none" stroke="#ddd" stroke-width="1.5"/></svg><span>hello@lumoride.example</span></li>
    </ul>
  </div>
</footer>
<div class="f-bottom">© 2018 Lumo Ride. All right reserved</div>

</body>
</html>
```